Bottle label - mead

We need a bottle label (logo) design for a new mead product as part of our Wandering Kettle Brewing Co. brand. There are two parts to this project. We need a logo design for the mead product which is placed on the front of a bottle wrap that has additional information on the back of the label.
Wandering Kettle Brewing Co. is a New Zealand craft beer brand that is expanding its product range to a new mead product.
Mead is an ancient honey based alcoholic beverage ranging between beer and wine. Mead has many different sub-styles. Our strategy is to position mead primarily to the beer drinkers.
Note: Most meads in New Zealand today are packaged and promoted as a “honey wine”. We want to break away from this positioning. We will be using bottles that are much more in tune with the beer industry.
Label dimensions: Approximately 80mm high and 150mm wide for the entire label which wraps around the bottle. The main graphic that will be visible on the front is approximately 50mm wide.
Target Market(s)
Our strategy is to position mead primarily to the beer drinkers.
Target age group 25 – 50. We want the label to:
• Represent the brand Wandering Kettle Brewing Co.
• Establish a recognizable “Mead” product offering within our brand
• Be classy and playful, highlight “mead” (not honey) as the product
• Sit comfortably on a shelf amongst beer labels and not look out of place but be distinguished from beer (and greatly distinguished from wine)
• Flexible - be a master template for our complete mead range where styles and flavor names and graphics can be added in as new products are commercialized
Requirements
Must have
- Must have the following elements on the front of the label:
- Existing Wandering Kettle Brewing Co corporate logo
- To be designed: Wandering Kettle Mead logo
- alcohol content: e.g. 10.5%
On the back of the bottle wrapper we need room for
- the story (about the product, about us)
- handcrafted in Auckland, New Zealand
- This product contains approximately 3 standard drinks
- website address (www.brewpage.example/WanderingKettle)
- barcode
Should not have
- any association with the traditional honey wine. We don't want images of bees, honey pots, bears.

```html
<!DOCTYPE html>
<html lang="en">
<head>
<meta charset="utf-8">
<title>Wandering Kettle Mead – Bottle Wrap Label</title>
<link rel="stylesheet" href="https://fonts.googleapis.com/css2?family=Arvo:wght@700&family=Arimo:wght@400&family=Archivo+Black&display=swap">
<style>
  :root {
    --paper: #f3f2f0;
    --label-dark: #4e1d12;
    --label-mid: #62291b;
    --label-light: #74382a;
    --cream: #f7efe6;
    --ink: #111111;
    --white: #ffffff;
    --gold: #d9b872;
    --rule: rgba(255, 255, 255, 0.55);
  }
  * { margin: 0; padding: 0; box-sizing: border-box; }
  html, body {
    width: 1047px;
    height: 1200px;
    overflow: hidden;
    background: var(--paper);
  }
  .canvas {
    position: relative;
    width: 1047px;
    height: 1200px;
  }
  .wrap-label {
    position: absolute;
    left: 18px;
    top: 138px;
    width: 1010px;
    height: 767px;
    background: radial-gradient(ellipse at 62% 40%, var(--label-light) 0%, var(--label-mid) 45%, var(--label-dark) 100%);
    overflow: hidden;
  }

  /* Back panel */
  .back-panel {
    position: absolute;
    left: 0;
    top: 0;
    width: 292px;
    height: 100%;
    color: var(--cream);
    font-family: "Arimo", Arial, sans-serif;
  }
  .back-brand {
    position: absolute;
    left: 26px;
    top: 30px;
    width: 250px;
    font-family: "Arvo", Georgia, serif;
    font-weight: 700;
    font-size: 30px;
    line-height: 1.1;
    color: var(--white);
  }
  .story-heading {
    position: absolute;
    left: 26px;
    top: 188px;
    font-family: "Arvo", Georgia, serif;
    font-weight: 700;
    font-size: 25px;
    letter-spacing: 1px;
    color: var(--white);
  }
  .story-text {
    position: absolute;
    left: 26px;
    top: 228px;
    width: 250px;
    font-size: 19px;
    line-height: 25.5px;
  }
  .back-rule {
    position: absolute;
    left: 26px;
    top: 490px;
    width: 250px;
    height: 1px;
    background: var(--rule);
  }
  .origin {
    position: absolute;
    left: 26px;
    top: 513px;
    width: 250px;
    font-size: 19px;
    line-height: 25px;
  }
  .standard-drinks {
    position: absolute;
    left: 26px;
    top: 628px;
    width: 250px;
    font-size: 14px;
  }
  .volume {
    position: absolute;
    left: 26px;
    top: 668px;
    font-size: 27px;
  }
  .website {
    position: absolute;
    left: 26px;
    top: 713px;
    font-size: 15px;
  }
  .panel-divider {
    position: absolute;
    left: 292px;
    top: 58px;
    width: 1px;
    height: 262px;
    background: var(--rule);
  }

  /* Front panel */
  .brand-disc {
    position: absolute;
    left: 487px;
    top: 24px;
    width: 280px;
    height: 280px;
    border-radius: 50%;
    background: var(--white);
    display: flex;
    align-items: center;
    justify-content: center;
    text-align: center;
  }
  .brand-disc-name {
    font-family: "Arvo", Georgia, serif;
    font-weight: 700;
    font-size: 30px;
    line-height: 1.15;
    color: var(--ink);
    width: 220px;
  }
  .mead-artwork {
    position: absolute;
    left: 387px;
    top: 300px;
    width: 540px;
    height: 450px;
  }
  .product-name {
    position: absolute;
    left: 462px;
    top: 448px;
    width: 340px;
    text-align: center;
    font-family: "Arvo", Georgia, serif;
    font-weight: 700;
    font-size: 104px;
    line-height: 1;
    color: var(--white);
  }
  .abv {
    position: absolute;
    left: 578px;
    top: 683px;
    width: 100px;
    text-align: center;
    font-family: "Archivo Black", Arial, sans-serif;
    font-size: 22px;
    color: var(--white);
  }
  .rating {
    position: absolute;
    left: 578px;
    top: 710px;
    width: 100px;
    text-align: center;
    font-size: 20px;
    letter-spacing: 6px;
    color: var(--gold);
  }
</style>
</head>
<body>
<main class="canvas">
  <section class="wrap-label" aria-label="Wandering Kettle Mead bottle wrap label">

    <div class="back-panel">
      <p class="back-brand">Wandering Kettle Brewing Co.</p>
      <h2 class="story-heading">OUR STORY</h2>
      <p class="story-text">Wandering Kettle Brewing Co creates fine mead at home in New Zealand. Description of product goes here. Wandering Kettle Brewing Co is a New Zealand maker of quality brews with a sense of adventure. Fresh and bold. Every bottle by hand.</p>
      <div class="back-rule"></div>
      <p class="origin">Handcrafted in Auckland, New Zealand</p>
      <p class="standard-drinks">Contains approx. 3 standard drinks</p>
      <p class="volume">330mL - 10.5%</p>
      <p class="website">www.brewpage.example/WanderingKettle</p>
    </div>
    <div class="panel-divider"></div>

    <div class="brand-disc">
      <p class="brand-disc-name">Wandering Kettle Brewing Co.</p>
    </div>

    <svg class="mead-artwork" viewBox="0 0 540 450" role="img" aria-label="Golden sunburst behind the Mead name, flanked by two sketched birds">
      <defs>
        <radialGradient id="burst-glow" cx="50%" cy="50%" r="50%">
          <stop offset="0%" stop-color="#fbd04a"/>
          <stop offset="50%" stop-color="#f6a21a"/>
          <stop offset="80%" stop-color="#e0571c" stop-opacity="0.55"/>
          <stop offset="100%" stop-color="#62291b" stop-opacity="0"/>
        </radialGradient>
      </defs>
      <ellipse cx="250" cy="230" rx="230" ry="190" fill="url(#burst-glow)"/>
    </svg>

    <h1 class="product-name">Mead</h1>

    <p class="abv">10.5%</p>
    <p class="rating" aria-label="Three stars">★★★</p>

  </section>
</main>
</body>
</html>
```